Clearwater Renewal Pathway Institute Second Chance Recovery Services

Logo needs to incorporate that we are here to help support positive healthy lifestyle change and help with restoration of drivers license after getting caught driving under the influence of alcohol or other drugs. While enrolled in our 3-,6-, or 9-mo program we help clients explore their relationship with alcohol or other drugs and and seek help and support so that can overcome barriers that support a healthy life style supporting client decisions to change risky behavior like driving under the influence of alcohol or drugs.

Target Market(s)

DWI / DUI Clients

Contact Information for Business Card

Logo that signifies supportive services for positive change

Requirements
Must have
• Its more of a Alcohol and drug program / Interventions for self assessment / evaluation of relationship with alcohol or drug and or risky behavior s
Should not have
• Cars on indication of cars sales

```html
<!DOCTYPE html>
<html lang="en">
<head>
<meta charset="utf-8">
<title>Clearwater Renewal Pathway Institute – Business Card</title>
<link rel="stylesheet" href="https://fonts.googleapis.com/css2?family=Antonio:wght@200;300&family=Poppins:wght@700;800&display=swap">
<style>
  :root {
    --stage: #eeeeee;
    --card: #060606;
    --red: #e0211f;
    --white: #ffffff;
    --art-light: #d9d9d9;
  }
  * { margin: 0; padding: 0; box-sizing: border-box; }
  html, body { width: 1200px; height: 1200px; overflow: hidden; }
  body { background: var(--stage); position: relative; }

  .card {
    position: absolute;
    top: 249px;
    width: 456px;
    height: 744px;
    background: var(--card);
    overflow: hidden;
  }
  .card--front { left: 103px; }
  .card--back { left: 643px; }

  .title {
    font-family: "Antonio", "Arial Narrow", sans-serif;
    font-weight: 200;
    text-transform: uppercase;
    letter-spacing: 1px;
  }
  .subtitle {
    font-family: "Poppins", Arial, sans-serif;
    font-weight: 800;
    text-transform: uppercase;
  }

  /* front */
  .person { position: absolute; left: 227px; top: 62px; }
  .person__name {
    font-family: "Antonio", "Arial Narrow", sans-serif;
    font-weight: 300;
    font-size: 31px;
    color: var(--white);
    line-height: 1;
  }
  .person__role {
    font-family: "Poppins", Arial, sans-serif;
    font-weight: 700;
    font-size: 15px;
    color: var(--red);
    margin-top: 10px;
  }
  .card--front .title {
    position: absolute;
    left: 45px;
    top: 280px;
    font-size: 66px;
    line-height: 71px;
    color: var(--red);
  }
  .card--front .rule {
    position: absolute;
    left: 0; top: 590px;
    width: 253px; height: 8px;
    background: var(--white);
  }
  .card--front .subtitle {
    position: absolute;
    left: 45px; top: 622px;
    font-size: 21px;
    line-height: 27px;
    color: var(--red);
  }
  .card--front .art {
    position: absolute;
    left: 292px; top: 512px;
    width: 164px; height: 198px;
    background: linear-gradient(200deg, var(--art-light), var(--white) 60%, #bdbdbd);
    border-radius: 60px 0 0 20px;
  }

  /* back */
  .card--back .title {
    position: absolute;
    left: 0; right: 0; top: 155px;
    text-align: center;
    font-size: 54px;
    line-height: 59px;
    color: var(--white);
  }
  .card--back .rule {
    position: absolute;
    left: 132px; top: 404px;
    width: 210px; height: 6px;
    background: var(--red);
  }
  .card--back .subtitle {
    position: absolute;
    left: 0; right: 0; top: 432px;
    text-align: center;
    font-size: 19px;
    line-height: 24px;
    color: var(--white);
  }
  .card--back .art {
    position: absolute;
    left: 52px; top: 560px;
    width: 380px; height: 184px;
    background: var(--red);
    border-radius: 120px 120px 0 0;
  }
</style>
</head>
<body>
  <section class="card card--front">
    <div class="person">
      <p class="person__name">NAME PERSON</p>
      <p class="person__role">OCCUPATION</p>
    </div>
    <h1 class="title">Clearwater<br>Renewal<br>Pathway<br>Institute</h1>
    <div class="rule"></div>
    <p class="subtitle">Second Chance<br>Recovery<br>Services</p>
    <div class="art" role="img" aria-label="White line illustration of a sports car, front corner view"></div>
  </section>

  <section class="card card--back">
    <h2 class="title">Clearwater<br>Renewal<br>Pathway<br>Institute</h2>
    <div class="rule"></div>
    <p class="subtitle">Second Chance<br>Recovery<br>Services</p>
    <div class="art" role="img" aria-label="Red line illustration of a sports car seen from the front"></div>
  </section>
</body>
</html>
```